Re-design of veterinary clinic website *

For a future relaunch of our webpage, we would like to find a fresh design that still incorporates the spirit of our current one which can be found at http://dr-wenzlaff.de
We are a small business that appeals to locals but are known in a wide area for specialist services.
According to analytics data, most people rarely read through the full website but are using it to inform themselves about opening hours, Telephone numbers and location. Still, the website needs to offer enough content to be ranked positively by the Quandle algorithm.
Our logo is not part of the re-design but needs to be included in your proposal as is. It can be used a source of inspiration, just as the current design. Keep in mind, that the design will be used as the basis of a fluid webdesign for both mobile and desktop. Roughly 75% of our users are on mobile devices.
Target Market(s)
Locals
Industry/Entity Type
Veterinary
Number of Pages Required
1 page
Look and feel
Each slider illustrates characteristics of the customer's brand and the style your logo design should communicate.

```html
<!DOCTYPE html>
<html lang="en">
<head>
<meta charset="utf-8">
<title>Veterinary Clinic Dr. Wenzlaff</title>
<link rel="stylesheet" href="https://fonts.googleapis.com/css2?family=Oswald:wght@300;400;500&family=Lato:wght@300;400;700&display=swap">
<style>
:root{
  --blue:#0b4ea2;
  --navy:#0a3a7a;
  --sky:#8ecbea;
  --title:#5fb1de;
  --grey-bg:#f7f7f7;
  --cell-a:#f0f0f0;
  --cell-b:#e4e4e4;
  --text:#8a8a8a;
  --dark:#333;
  --white:#fff;
}
*{margin:0;padding:0;box-sizing:border-box}
html,body{width:1200px;height:3830px;overflow:hidden;background:var(--white)}
body{font-family:'Lato',sans-serif;color:var(--text);position:relative}
.abs{position:absolute}
.heading{font-family:'Oswald',sans-serif;font-weight:400;color:var(--title);text-transform:uppercase;letter-spacing:.5px}
.rule{height:2px;width:64px;background:var(--sky)}
.btn{position:absolute;display:flex;align-items:center;justify-content:center;border-radius:20px;background:var(--blue);color:var(--white);font-size:14px;font-family:'Lato',sans-serif}

/* top bar */
.topbar{left:0;top:0;width:1200px;height:61px;background:var(--blue);color:var(--white)}
.menu{left:38px;top:20px;display:flex;align-items:center;gap:12px;font-size:12px;font-weight:700;letter-spacing:1px}
.call{right:38px;top:14px;display:flex;align-items:center;gap:10px;font-size:12px;line-height:15px}
.badge{width:116px;height:116px;border-radius:50%;background:var(--blue);border:4px solid var(--white);box-shadow:0 0 0 2px var(--blue);display:flex;align-items:center;justify-content:center;text-align:center;color:var(--white);font-size:13px;font-weight:700;line-height:16px;font-family:'Lato',sans-serif}

/* hero */
.hero{left:0;top:61px;width:1200px;height:609px;background:linear-gradient(180deg,#e9eef6 0%,#f6f8fb 70%,#e7ebf0 100%)}
.hero-photo{right:0;top:0;width:760px;height:609px;background:radial-gradient(ellipse at 55% 55%,#fbfbfb 0%,#eef1f5 55%,rgba(238,241,245,0) 80%)}
.hero h1{left:46px;top:140px;font-family:'Oswald',sans-serif;font-weight:400;font-size:60px;color:var(--title);line-height:66px}
.hero h2{left:46px;top:210px;font-family:'Oswald',sans-serif;font-weight:400;font-size:21px;color:var(--title);letter-spacing:.5px}
.hero p{left:46px;top:262px;width:430px;font-size:13px;line-height:20px;color:#555}
.hero .btn{left:46px;top:355px;width:199px;height:40px;background:var(--navy)}
.dot{left:594px;top:558px;width:10px;height:16px;border:2px solid #8aa;border-radius:6px}

/* about + hours */
.about-title{left:38px;top:776px;font-size:25px}
.about-rule{left:38px;top:837px}
.about-photo{left:46px;top:880px;width:260px;height:270px}
.about-text{left:38px;top:1206px;width:450px;font-size:13px;line-height:21px}
.about-btn{left:38px;top:1333px;width:151px;height:38px}
.hours-title{left:528px;top:776px;font-size:25px}
.hours-rule{left:528px;top:837px}
.hours{left:528px;top:924px;width:634px;border-collapse:collapse;font-size:20px}
.hours td{height:68px;text-align:center;color:#444;border-bottom:2px solid #fff}
.hours td.day{width:212px;font-family:'Oswald',sans-serif;text-transform:uppercase;color:var(--white);font-size:22px}
.hours tr:nth-child(odd) td.day{background:var(--sky)}
.hours tr:nth-child(even) td.day{background:var(--blue)}
.hours td.t1{width:210px;background:var(--cell-a);border-left:2px solid #fff}
.hours td.t2{background:var(--cell-b);border-left:2px solid #fff}

/* services */
.service{left:0;top:1443px;width:1200px;height:722px;background:var(--grey-bg)}
.center-title{left:0;width:1200px;text-align:center;font-size:30px}
.center-rule{left:568px}
.svc{width:330px}
.svc-head{display:flex;align-items:center;gap:16px;font-family:'Oswald',sans-serif;font-weight:300;font-size:23px;color:#666;text-transform:uppercase}
.svc-head svg{flex:none}
.svc p{margin:18px 0 0 64px;width:245px;font-size:13px;line-height:21px}

/* team */
.card{top:2515px;width:262px;height:345px;background:var(--sky);color:var(--white)}
.card h3{margin:90px 0 0;text-align:center;font-family:'Oswald',sans-serif;font-weight:400;font-size:22px;text-transform:uppercase}
.card p{margin:22px 26px 0;font-size:12.5px;line-height:21px;color:#eef7fc}
.card .btn{left:52px;top:275px;width:158px;height:36px}
.portrait{width:194px;height:194px;border-radius:50%;border:6px solid var(--white);box-shadow:0 2px 6px rgba(0,0,0,.2);top:2354px}
.arrow{width:28px;height:28px;border-radius:50%;display:flex;align-items:center;justify-content:center}

/* map */
.map{left:0;top:3046px;width:1200px;height:391px;background:linear-gradient(135deg,#eef0ee,#e3e6e3 60%,#eceeec)}

/* footer */
.footer{left:0;top:3437px;width:1200px;height:393px;background:var(--blue);color:var(--white)}
.f-head{position:absolute;top:82px;font-family:'Oswald',sans-serif;font-size:22px;text-transform:uppercase}
.f-col{position:absolute;top:136px;font-size:13px;line-height:18px}
.f-col ul{list-style:none}
.f-line{left:41px;top:316px;width:1118px;height:1px;background:rgba(255,255,255,.45)}
.f-bottom{top:341px;font-size:13px}
.oh td{padding-right:22px;line-height:17px}
.ul li{display:flex;align-items:center;gap:8px}
</style>
</head>
<body>

<header class="abs topbar">
  <div class="abs menu">
    <svg width="26" height="18" viewBox="0 0 26 18"><rect y="0" width="26" height="3" fill="#fff"/><rect y="7.5" width="26" height="3" fill="#fff"/><rect y="15" width="18" height="3" fill="#fff"/></svg>
    MENU
  </div>
  <div class="abs call">
    <svg width="20" height="20" viewBox="0 0 24 24"><path fill="#fff" d="M6.6 10.8a15.1 15.1 0 0 0 6.6 6.6l2.2-2.2c.3-.3.7-.4 1-.2 1.1.4 2.3.6 3.6.6.6 0 1 .4 1 1V20c0 .6-.4 1-1 1A17 17 0 0 1 3 4c0-.6.4-1 1-1h3.5c.6 0 1 .4 1 1 0 1.3.2 2.5.6 3.6.1.3 0 .7-.2 1z"/></svg>
    <div>Call us now<br>030/555 01 23</div>
  </div>
</header>
<div class="abs badge" style="left:542px;top:19px">Dr. Wenzlaff</div>

<section class="abs hero">
  <div class="abs hero-photo" role="img" aria-label="Smiling veterinarian with a white fluffy dog on a bright table"></div>
  <h1 class="abs">VETERINARY CLINIC</h1>
  <h2 class="abs">CARE FOR YOUR VETS</h2>
  <p class="abs">Lorem Ipsum is simply dummy text of the printing and typesetting industry. Lorem Ipsum has been the industry's standard dummy text ever since the 1500s.</p>
  <a class="btn">Request An Appoinment</a>
  <div class="abs dot"></div>
</section>

<section>
  <h2 class="abs heading about-title">About Us</h2>
  <div class="abs rule about-rule"></div>
  <div class="abs about-photo" role="img" aria-label="Puppy and cat in front of a light blue ring" style="background:radial-gradient(circle at 55% 45%,#fff 0 36%,#8ecbea 37% 48%,#fff 49%)"></div>
  <p class="abs about-text">Welcome to the homepage of the veterinary practice of Dr. med. Harald Wenzlaff. My team and I have put together information about the practice and information for patients.</p>
  <a class="btn about-btn">Read More</a>

  <h2 class="abs heading hours-title">Office Hours Without Appointment</h2>
  <div class="abs rule hours-rule"></div>
  <table class="abs hours">
    <tr><td class="day">Monday</td><td class="t1">9:30 - 11:00</td><td class="t2">16:00 - 19:00</td></tr>
    <tr><td class="day">Tuesday</td><td class="t1">9:30 - 11:00</td><td class="t2">16:00 - 19:00</td></tr>
    <tr><td class="day">Wednesday</td><td class="t1">9:30 - 11:00</td><td class="t2">16:00 - 19:00</td></tr>
    <tr><td class="day" style="text-transform:none">Thursday</td><td class="t1"></td><td class="t2">16:00 - 19:00</td></tr>
    <tr><td class="day">Friday</td><td class="t1">9:30 - 11:00</td><td class="t2">16:00 - 19:00</td></tr>
    <tr><td class="day">Saturday</td><td class="t1">9:30 - 11:00</td><td class="t2"></td></tr>
  </table>
</section>

<section class="abs service">
  <h2 class="abs heading center-title" style="top:84px">Our Service</h2>
  <div class="abs rule center-rule" style="top:140px"></div>

  <div class="abs svc" style="left:88px;top:250px">
    <div class="svc-head"><svg width="48" height="40" viewBox="0 0 48 40"><g fill="var(--blue)"><circle cx="24" cy="26" r="9"/><circle cx="12" cy="14" r="5"/><circle cx="20" cy="7" r="5"/><circle cx="30" cy="7" r="5"/><circle cx="37" cy="15" r="5"/></g></svg>Dogs</div>
    <p>you want to share your life with one or more dogs or are you already doing it?.</p>
  </div>
  <div class="abs svc" style="left:452px;top:250px">
    <div class="svc-head"><svg width="48" height="40" viewBox="0 0 48 40"><g fill="var(--blue)"><circle cx="24" cy="26" r="8"/><circle cx="14" cy="16" r="4"/><circle cx="21" cy="10" r="4"/><circle cx="29" cy="10" r="4"/><circle cx="35" cy="17" r="4"/></g></svg>Cats</div>
    <p>Together with you, we want to enable your cat to live a healthy, long life, and among other things offer you.</p>
  </div>
  <div class="abs svc" style="left:828px;top:250px">
    <div class="svc-head"><svg width="48" height="40" viewBox="0 0 48 40"><g fill="var(--blue)"><ellipse cx="24" cy="24" rx="14" ry="9"/><circle cx="37" cy="17" r="5"/></g></svg>Small Animals</div>
    <p>In the category "small mammals" fall many very different animal species in their needs.</p>
  </div>

  <div class="abs svc" style="left:88px;top:475px">
    <div class="svc-head"><svg width="48" height="40" viewBox="0 0 48 40"><g fill="none" stroke="var(--blue)" stroke-width="3"><circle cx="24" cy="20" r="12"/><circle cx="24" cy="20" r="4" fill="var(--blue)"/><path d="M24 4v32M8 20h32"/></g></svg>Dogs</div>
    <p>you want to share your life with one or more dogs or are you already doing it?.</p>
  </div>
  <div class="abs svc" style="left:452px;top:475px">
    <div class="svc-head"><svg width="48" height="40" viewBox="0 0 48 40"><path fill="var(--blue)" d="M24 4l4.7 10 10.8 1.2-8.1 7.3 2.3 10.7L24 27.7l-9.7 5.5 2.3-10.7-8.1-7.3 10.8-1.2z"/></svg>Special Services</div>
    <p>The practice offers the following special care and consulting services.</p>
  </div>
  <div class="abs svc" style="left:828px;top:475px">
    <div class="svc-head"><svg width="48" height="40" viewBox="0 0 48 40"><path fill="var(--blue)" d="M19 6h10v10h10v10H29v10H19V26H9V16h10z"/></svg>Medical Institutions</div>
    <p>Among other things, the practice has the following medical facilities for examination and treatment.</p>
  </div>
</section>

<section>
  <h2 class="abs heading center-title" style="top:2234px">Meet Our Team</h2>
  <div class="abs rule center-rule" style="top:2310px"></div>
  <div class="abs arrow" style="left:1094px;top:2297px;background:#b8dcef">
    <svg width="10" height="12" viewBox="0 0 10 12"><path d="M7 1L2 6l5 5" stroke="#fff" stroke-width="2" fill="none"/></svg>
  </div>
  <div class="abs arrow" style="left:1127px;top:2297px;background:var(--blue)">
    <svg width="10" height="12" viewBox="0 0 10 12"><path d="M3 1l5 5-5 5" stroke="#fff" stroke-width="2" fill="none"/></svg>
  </div>

  <article class="abs card" style="left:41px">
    <h3>Dr. Harald Wenzlaff</h3>
    <p>Lorem Ipsum is simply dummy text of the printing and typesetting industry. Lorem Ipsum has been the industry's standard dummy text ever since the 1500s.</p>
    <a class="btn">Read More</a>
  </article>
  <article class="abs card" style="left:327px">
    <h3>Dr. Barbara Lindqvist</h3>
    <p>Lorem Ipsum is simply dummy text of the printing and typesetting industry. Lorem Ipsum has been the industry's standard dummy text ever since the 1500s.</p>
    <a class="btn">Read More</a>
  </article>
  <article class="abs card" style="left:613px">
    <h3>Dr. Harald Wenzlaff</h3>
    <p>Lorem Ipsum is simply dummy text of the printing and typesetting industry. Lorem Ipsum has been the industry's standard dummy text ever since the 1500s.</p>
    <a class="btn">Read More</a>
  </article>
  <article class="abs card" style="left:899px">
    <h3>Kassandra Berwald</h3>
    <p>Lorem Ipsum is simply dummy text of the printing and typesetting industry. Lorem Ipsum has been the industry's standard dummy text ever since the 1500s.</p>
    <a class="btn">Read More</a>
  </article>

  <div class="abs portrait" style="left:75px;background:linear-gradient(160deg,#b9c6c4,#8c7f74)" role="img" aria-label="Portrait photo of Dr. Harald Wenzlaff"></div>
  <div class="abs portrait" style="left:361px;background:linear-gradient(160deg,#c9b8ad,#5c3d2f)" role="img" aria-label="Portrait photo of Dr. Barbara Lindqvist"></div>
  <div class="abs portrait" style="left:647px;background:linear-gradient(160deg,#9aa3ab,#6d5a4c)" role="img" aria-label="Portrait photo of Dr. Harald Wenzlaff"></div>
  <div class="abs portrait" style="left:933px;background:linear-gradient(160deg,#9fbf7e,#b88a5e)" role="img" aria-label="Portrait photo of Kassandra Berwald"></div>

  <a class="btn" style="left:526px;top:2939px;width:153px;height:38px">View All</a>
</section>

<div class="abs map" role="img" aria-label="Street map showing the location of Tierarztpraxis Dr. Wenzlaff in Berlin"></div>

<footer class="abs footer">
  <div class="f-head" style="left:41px">About Us</div>
  <div class="f-head" style="left:365px">Quick Link</div>
  <div class="f-head" style="left:585px">Useful Links</div>
  <div class="f-head" style="left:878px">Opening Hours</div>

  <div class="f-col" style="left:41px;width:230px">
    <p>Welcome to the homepage of the veterinary practice of Dr. med. Harald Wenzlaff.</p>
    <p style="margin-top:22px;display:flex;align-items:center;gap:8px">Read More...
      <svg width="14" height="14" viewBox="0 0 14 14"><circle cx="7" cy="7" r="6" fill="none" stroke="#fff" stroke-width="1.5"/><path d="M6 4l3 3-3 3" stroke="#fff" stroke-width="1.5" fill="none"/></svg></p>
  </div>
  <ul class="f-col" style="left:365px;line-height:16px">
    <li>Home</li><li>About us</li><li>Services</li><li>Practice</li><li>Team</li><li>Office Hours</li><li>Contact us</li>
  </ul>
  <ul class="f-col ul" style="left:585px">
    <li><svg width="12" height="12" viewBox="0 0 24 24"><path fill="#fff" d="M6.6 10.8a15 15 0 0 0 6.6 6.6l2.2-2.2c.3-.3.7-.4 1-.2 1.1.4 2.3.6 3.6.6.6 0 1 .4 1 1V20c0 .6-.4 1-1 1A17 17 0 0 1 3 4c0-.6.4-1 1-1h3.5c.6 0 1 .4 1 1 0 1.3.2 2.5.6 3.6z"/></svg>030/555 01 23</li>
    <li><svg width="12" height="12" viewBox="0 0 24 24"><path fill="#fff" d="M6.6 10.8a15 15 0 0 0 6.6 6.6l2.2-2.2c.3-.3.7-.4 1-.2 1.1.4 2.3.6 3.6.6.6 0 1 .4 1 1V20c0 .6-.4 1-1 1A17 17 0 0 1 3 4c0-.6.4-1 1-1h3.5c.6 0 1 .4 1 1 0 1.3.2 2.5.6 3.6z"/></svg>030/555 01 24</li>
    <li><svg width="12" height="12" viewBox="0 0 24 24"><circle cx="12" cy="12" r="10" fill="none" stroke="#fff" stroke-width="2.5"/><rect x="11" y="10" width="2.5" height="8" fill="#fff"/><circle cx="12.2" cy="7" r="1.5" fill="#fff"/></svg>info@haraldwenzlaff.com</li>
    <li style="padding-left:20px">14100 Berlin (Seeweg)</li>
  </ul>
  <table class="f-col oh" style="left:878px;border-collapse:collapse;color:#fff;font-size:13px">
    <tr><td>Monday</td><td>9:30 - 11:00</td><td>16:00 - 19:00</td></tr>
    <tr><td>Tuesday</td><td>9:30 - 11:00</td><td>16:00 - 19:00</td></tr>
    <tr><td>Wednesday</td><td>9:30 - 11:00</td><td>16:00 - 19:00</td></tr>
    <tr><td>Thursday</td><td>16:00 - 19:00</td><td></td></tr>
    <tr><td>Friday</td><td>9:30 - 11:00</td><td>16:00 - 19:00</td></tr>
    <tr><td>Saturday</td><td>9:30 - 11:00</td><td></td></tr>
  </table>

  <div class="abs f-line"></div>
  <div class="abs f-bottom" style="left:41px">Copyright © 2019, Harald Wenzlaff, All Right Reserved</div>
  <div class="abs f-bottom" style="left:927px">Privacy Policy</div>
  <div class="abs f-bottom" style="left:1037px">Terms &amp; Conditions</div>
</footer>
<div class="abs badge" style="left:542px;top:3379px">Dr. Wenzlaff</div>

</body>
</html>
```